Management Consultancy needs sharp professional services showcased in a brochure

We are a management consultancy specializing on contract management and conflict avoidance services requiring a professional brochure showcasing our services to prospective clients.

Attached are a selection of existing stationary and the colour scheme.

Further details on our company can be found at www.velto-advisory-partners.com
Updates

Preference is for bi-fold, however, innovative tri-fold will be considered. Added Monday, August 7, 2017

Target Market(s)

Construction companies, consultants, developers, oil and gas service providers, NGO's, SME's.

Industry/Entity Type

Management

Requirements
Must have
• High degree of professionalism with eye catching, sharp detail. No frils.
• Colour scheme as per the attachments
• Font as per attachments - Century Gothic
• Details of our company and services
Nice to have
• Open to ideas, thinking along the lines of a car brochure type design.
• Bi-fold preferred, by trifold accepted if innovative.
Should not have
• Remove reference to the United Arab Emirates.
• No cartoon/clipart photos.

```html
<!DOCTYPE html>
<html lang="en">
<head>
<meta charset="utf-8">
<title>Velto Advisory – Tri-fold Brochure</title>
<link href="https://fonts.googleapis.com/css2?family=Cinzel:wght@400;600&family=Didact+Gothic&family=Questrial&display=swap" rel="stylesheet">
<style>
  :root{
    --bg:#6d6d6d;
    --paper:#ffffff;
    --navy:#1f3a64;
    --steel:#3c5f88;
    --red:#d1202f;
    --ink:#3a3a3a;
    --photo-a:#d9d6d2;
    --photo-b:#7a6a5c;
  }
  *{box-sizing:border-box;margin:0;padding:0}
  html,body{width:1200px;height:1200px;overflow:hidden;background:var(--bg)}
  body{font-family:"Didact Gothic","Questrial",sans-serif;color:var(--ink)}
  .sheet{position:absolute;left:90px;top:200px;width:1020px;height:800px;display:flex;background:var(--paper);box-shadow:0 20px 40px rgba(0,0,0,.35)}
  .panel{position:relative;width:340px;height:800px;overflow:hidden}
  .panel + .panel{border-left:1px solid #ececec}

  /* services panel */
  .services{padding:40px 22px 0 26px}
  .tag{display:inline-block;color:#fff;font-family:"Questrial",sans-serif;font-size:11px;padding:3px 14px 3px 18px;margin-left:-26px;border-radius:0 10px 10px 0}
  .tag--red{background:var(--red)}
  .tag--blue{background:var(--steel)}
  .body-copy{font-size:9.4px;line-height:1.42;text-align:justify;margin:10px 0 12px}
  .checklist{list-style:none;margin:8px 0 14px}
  .checklist li{position:relative;padding-left:16px;font-size:9.6px;line-height:1.35;margin-bottom:8px}
  .checklist svg,.sectors svg{position:absolute;left:0;top:1px;width:10px;height:10px}
  .services .rule{position:absolute;left:0;right:0;height:5px}
  .services .rule--steel{bottom:62px;background:var(--steel)}
  .services .rule--red{bottom:54px;height:3px;background:var(--red)}

  /* about panel */
  .about{padding:44px 24px 0 24px}
  .lead{color:var(--navy);font-weight:700;font-size:11px;line-height:1.35;text-align:justify;font-family:"Questrial",sans-serif;letter-spacing:.2px}
  .sectors{list-style:none;margin:16px 0 18px}
  .sectors li{position:relative;padding-left:22px;font-size:10px;line-height:1.35;color:#222;font-weight:700}
  .sectors svg{left:4px}
  .about .body-copy{font-size:9.8px;margin:0 0 14px}
  .about-copy{position:relative}
  .about-photo{position:absolute;left:0;top:420px;width:340px;height:180px;background:linear-gradient(180deg,#fff 0%,#e7e9ec 50%,#eef0f2 100%)}
  .about .rule{position:absolute;left:0;right:0;top:600px;height:3px;background:var(--red)}
  .brand{font-family:"Cinzel",serif;font-weight:600;color:var(--navy);letter-spacing:.5px}
  .about .brand{position:absolute;right:26px;top:640px;font-size:17px}
  .contact{position:absolute;right:26px;font-size:10.5px;display:flex;align-items:center;gap:8px;color:#222}
  .contact svg{width:12px;height:12px}
  .contact--mail{top:690px}
  .contact--web{top:716px}

  /* cover panel */
  .cover .brand{position:absolute;left:0;right:0;top:72px;text-align:center;font-size:20px}
  .cover-photo{position:absolute;left:0;top:140px;width:340px;height:460px;background:linear-gradient(180deg,#eef0f2 0%,var(--photo-a) 20%,#a79484 55%,var(--photo-b) 100%)}
  .cover .rule{position:absolute;left:0;right:0}
  .cover .rule--red{top:600px;height:3px;background:var(--red)}
  .cover .rule--steel{top:606px;height:5px;background:var(--steel)}
  .cover-title{position:absolute;left:0;right:0;top:640px;text-align:center;font-family:"Cinzel",serif;font-weight:400;line-height:1.2}
  .cover-title span{display:block}
  .cover-title .t1{color:var(--navy);font-size:23px}
  .cover-title .t2{color:var(--navy);font-size:19px}
  .cover-title .t3{color:var(--red);font-size:22px}
  .url-bar{position:absolute;left:0;right:0;top:742px;height:26px;background:var(--steel);color:#fff;font-size:10.5px;letter-spacing:2px;display:flex;align-items:center;justify-content:center}
</style>
</head>
<body>
<main class="sheet">
  <section class="panel services">
    <span class="tag tag--red">Our Services</span>
    <p class="body-copy">Every contract has at least two parties; every party has a goal, and every goal matters. Each party must work in equilibrium as a contractual partnership or alliance. It is on this premise we aim to deliver truly mutual agreements, maintaining the contract integrity from inception through the contract life, and where we are not party to the original agreement, we provide effective solutions to contractual conflict via our unique mediation methodology at all positions of the conflict cycle and aim to enhance all aspects of contract performance by effective audit and management.</p>
    <p class="body-copy">We believe that a proactive approach to contract management creates transparency and trust, and maintains relationships and builds on them for the future whilst cultivating significant value to your business transactions and addressing real and relevant issues, providing and implementing effective solutions. We believe that avoidance of contractual conflict and timely resolution on escalation is paramount in the effectiveness of any agreement.</p>

    <span class="tag tag--blue">Conflict Advisory</span>
    <ul class="checklist">
      <li><svg viewBox="0 0 10 10"><circle cx="5" cy="5" r="4.2" fill="none" stroke="var(--red)" stroke-width="1.2"/><path d="M3 5.2 4.5 6.6 7.2 3.6" fill="none" stroke="var(--red)" stroke-width="1.2"/></svg>Restoration and Mediation Services.</li>
      <li><svg viewBox="0 0 10 10"><circle cx="5" cy="5" r="4.2" fill="none" stroke="var(--red)" stroke-width="1.2"/><path d="M3 5.2 4.5 6.6 7.2 3.6" fill="none" stroke="var(--red)" stroke-width="1.2"/></svg>Shuttle Diplomacy Services and In Persona Intermediary Services.</li>
      <li><svg viewBox="0 0 10 10"><circle cx="5" cy="5" r="4.2" fill="none" stroke="var(--red)" stroke-width="1.2"/><path d="M3 5.2 4.5 6.6 7.2 3.6" fill="none" stroke="var(--red)" stroke-width="1.2"/></svg>Negotiation Support Services.</li>
      <li><svg viewBox="0 0 10 10"><circle cx="5" cy="5" r="4.2" fill="none" stroke="var(--red)" stroke-width="1.2"/><path d="M3 5.2 4.5 6.6 7.2 3.6" fill="none" stroke="var(--red)" stroke-width="1.2"/></svg>Workplace/Corporate Mediation Services.</li>
    </ul>

    <span class="tag tag--blue">Contract Advisory</span>
    <ul class="checklist">
      <li><svg viewBox="0 0 10 10"><circle cx="5" cy="5" r="4.2" fill="none" stroke="var(--red)" stroke-width="1.2"/><path d="M3 5.2 4.5 6.6 7.2 3.6" fill="none" stroke="var(--red)" stroke-width="1.2"/></svg>Contract Troubleshooting.</li>
      <li><svg viewBox="0 0 10 10"><circle cx="5" cy="5" r="4.2" fill="none" stroke="var(--red)" stroke-width="1.2"/><path d="M3 5.2 4.5 6.6 7.2 3.6" fill="none" stroke="var(--red)" stroke-width="1.2"/></svg>Tender Review and Bid Support.</li>
      <li><svg viewBox="0 0 10 10"><circle cx="5" cy="5" r="4.2" fill="none" stroke="var(--red)" stroke-width="1.2"/><path d="M3 5.2 4.5 6.6 7.2 3.6" fill="none" stroke="var(--red)" stroke-width="1.2"/></svg>Direct and Third Party Contracts Audit Services and Performance Management.</li>
      <li><svg viewBox="0 0 10 10"><circle cx="5" cy="5" r="4.2" fill="none" stroke="var(--red)" stroke-width="1.2"/><path d="M3 5.2 4.5 6.6 7.2 3.6" fill="none" stroke="var(--red)" stroke-width="1.2"/></svg>Strategic Review &amp; Risk Assessment.</li>
      <li><svg viewBox="0 0 10 10"><circle cx="5" cy="5" r="4.2" fill="none" stroke="var(--red)" stroke-width="1.2"/><path d="M3 5.2 4.5 6.6 7.2 3.6" fill="none" stroke="var(--red)" stroke-width="1.2"/></svg>Contract Fraud Investigation.</li>
      <li><svg viewBox="0 0 10 10"><circle cx="5" cy="5" r="4.2" fill="none" stroke="var(--red)" stroke-width="1.2"/><path d="M3 5.2 4.5 6.6 7.2 3.6" fill="none" stroke="var(--red)" stroke-width="1.2"/></svg>Temporary Placement Contract Management Solutions.</li>
    </ul>
    <div class="rule rule--steel"></div>
    <div class="rule rule--red"></div>
  </section>

  <section class="panel about">
    <div class="about-photo" role="img" aria-label="Faded photo of a business meeting with hands over documents"></div>
    <div class="about-copy">
      <p class="lead">We are an experienced contract and conflict advisory providing global contract performance solutions and conflict management to:</p>
      <ul class="sectors">
        <li><svg viewBox="0 0 10 10"><circle cx="5" cy="5" r="4.2" fill="none" stroke="var(--red)" stroke-width="1.2"/><path d="M3 5.2 4.5 6.6 7.2 3.6" fill="none" stroke="var(--red)" stroke-width="1.2"/></svg>international development organisations</li>
        <li><svg viewBox="0 0 10 10"><circle cx="5" cy="5" r="4.2" fill="none" stroke="var(--red)" stroke-width="1.2"/><path d="M3 5.2 4.5 6.6 7.2 3.6" fill="none" stroke="var(--red)" stroke-width="1.2"/></svg>construction industry</li>
        <li><svg viewBox="0 0 10 10"><circle cx="5" cy="5" r="4.2" fill="none" stroke="var(--red)" stroke-width="1.2"/><path d="M3 5.2 4.5 6.6 7.2 3.6" fill="none" stroke="var(--red)" stroke-width="1.2"/></svg>oil and gas industry</li>
        <li><svg viewBox="0 0 10 10"><circle cx="5" cy="5" r="4.2" fill="none" stroke="var(--red)" stroke-width="1.2"/><path d="M3 5.2 4.5 6.6 7.2 3.6" fill="none" stroke="var(--red)" stroke-width="1.2"/></svg>government sectors.</li>
      </ul>
      <p class="body-copy">Observing the standard of consultancy services and magnitude of contractual engagements and conflicts, we see the opportunity to make things better, better engagements, better awareness, better performance, which all lead to better value in terms of financial benefit and relationship maintenance. We firmly believe in party success in a non litigious environment.</p>
      <p class="body-copy">Our services are uniquely delivered through our integrated management consultancy model, with a single point of contact and responsibility, and focused attention to detail. We provide advisory services and solutions resolving past and current claims, and in doing so, preparing our clients for a conflict free future based on our core principles of integrity, equality and strength, ensuring compliance and experience at an intimate professional level. We aim to have our clients feel our principles in our presence and in our advisories, giving the service which is deserved.</p>
      <p class="body-copy">Our clients range from global top-tier multinational companies, international contractors to government bodies and authorities.</p>
    </div>
    <div class="rule"></div>
    <div class="brand">Velto Advisory</div>
    <div class="contact contact--mail">mhale@velto-advisory-partners.com
      <svg viewBox="0 0 12 12"><rect x="1" y="2.5" width="10" height="7" rx="1" fill="var(--navy)"/><path d="M1.5 3 6 6.5 10.5 3" fill="none" stroke="#fff" stroke-width="1"/></svg>
    </div>
    <div class="contact contact--web">www.velto-advisory-partners.com
      <svg viewBox="0 0 12 12"><circle cx="6" cy="6" r="5" fill="none" stroke="var(--navy)" stroke-width="1.1"/><ellipse cx="6" cy="6" rx="2.2" ry="5" fill="none" stroke="var(--navy)" stroke-width="1"/><path d="M1 6h10M2 3.5h8M2 8.5h8" stroke="var(--navy)" stroke-width=".9"/></svg>
    </div>
  </section>

  <section class="panel cover">
    <div class="brand">Velto Advisory</div>
    <div class="cover-photo" role="img" aria-label="Photo of three smiling consultants in business suits"></div>
    <div class="rule rule--red"></div>
    <div class="rule rule--steel"></div>
    <h1 class="cover-title"><span class="t1">The Contract</span><span class="t2">and</span><span class="t3">Conflict Advisory</span></h1>
    <div class="url-bar">www.velto-advisory-partners.com</div>
  </section>
</main>
</body>
</html>
```